Business Card New Design for Veltrix

We would like a new look on our business card, using the same style, the same colors blue, gray and white with similar font that is represented on the new Sell Sheet. We recently re-designed our Sell Sheets - I've attached a sell sheet file for your reference. I've also attached our current business card and our logo. Keep the same information listed on each side of the card.

Contact Information for Business Card

Use details given on example provided

Font styles to use
Other font styles liked:
• Myriad Regular and Bold

Colors

Designer to choose colors to be used in the design.

Requirements
Must have
• Current Information that was provided on the current business card. Colors Must use Blue, Gray and White, the same colors as the sell sheet example.

```html
<!DOCTYPE html>
<html lang="en">
<head>
<meta charset="utf-8">
<title>Veltrix Business Card</title>
<link href="https://fonts.googleapis.com/css2?family=PT+Sans:wght@400;700&display=swap" rel="stylesheet">
<style>
  :root {
    --brand-blue: #2328dd;
    --ink-gray: #3a3a3a;
    --rule-gray: #9a9a9a;
    --paper: #ffffff;
    --backdrop: #d9d9d9;
  }
  * { margin: 0; padding: 0; box-sizing: border-box; }
  html, body { width: 1200px; height: 800px; overflow: hidden; }
  body {
    background: var(--backdrop);
    font-family: "PT Sans", Arial, sans-serif;
    position: relative;
  }
  .card {
    position: absolute;
    left: 300px;
    width: 600px;
    height: 343px;
    border-radius: 22px;
    box-shadow: 0 6px 18px rgba(0,0,0,0.18);
    overflow: hidden;
  }
  .card--front { top: 36px; background: var(--paper); }
  .card--back { top: 420px; background: var(--brand-blue); color: var(--paper); }

  .front__brand {
    position: absolute;
    left: 0; top: 0;
    width: 290px; height: 343px;
    display: flex; align-items: center; justify-content: center;
  }
  .brand-name {
    font-weight: 400;
    letter-spacing: 0.22em;
    text-transform: uppercase;
  }
  .front__brand .brand-name { color: var(--brand-blue); font-size: 40px; }

  .front__divider {
    position: absolute;
    left: 300px; top: 60px;
    width: 1px; height: 222px;
    background: var(--rule-gray);
  }
  .front__details {
    position: absolute;
    left: 330px; top: 62px;
    color: var(--ink-gray);
    font-size: 14px;
    line-height: 1.35;
  }
  .person-name { color: var(--brand-blue); font-size: 26px; font-weight: 700; line-height: 1.1; }
  .person-title { font-size: 14px; margin-bottom: 12px; }
  .company-address { margin-bottom: 8px; }
  .contact-list { list-style: none; }
  .contact-list li { display: flex; align-items: center; gap: 8px; }
  .contact-icon { width: 12px; height: 12px; flex: none; }

  .back__brand {
    position: absolute;
    top: 92px; left: 0; width: 100%;
    text-align: center;
  }
  .back__brand .brand-name { font-size: 52px; color: var(--paper); }
  .service-list {
    position: absolute;
    top: 210px; left: 30px; right: 30px;
    text-align: center;
    font-size: 15px;
    line-height: 1.4;
  }
</style>
</head>
<body>
  <section class="card card--front">
    <div class="front__brand"><span class="brand-name">Veltrix</span></div>
    <div class="front__divider"></div>
    <div class="front__details">
      <p class="person-name">Daniel Hart</p>
      <p class="person-title">CEO</p>
      <p class="company-address">Veltrix Technical Services, Inc.<br>4170 Harbor Mill Road<br>Ashford, IL 60518</p>
      <ul class="contact-list">
        <li><svg class="contact-icon" viewBox="0 0 12 12"><path d="M2 1h3l1 3-1.5 1a6 6 0 0 0 2.5 2.5L8 6l3 1v3a1 1 0 0 1-1 1A9 9 0 0 1 1 2a1 1 0 0 1 1-1z" fill="#2328dd"/></svg>(800) 555-0142 x226</li>
        <li><svg class="contact-icon" viewBox="0 0 12 12"><path d="M2 1h3l1 3-1.5 1a6 6 0 0 0 2.5 2.5L8 6l3 1v3a1 1 0 0 1-1 1A9 9 0 0 1 1 2a1 1 0 0 1 1-1z" fill="#2328dd"/></svg>(815) 555-0142</li>
        <li><svg class="contact-icon" viewBox="0 0 12 12"><rect x="1.5" y="1.5" width="9" height="9" fill="none" stroke="#2328dd" stroke-width="1.5"/></svg>(815) 555-0187</li>
        <li><svg class="contact-icon" viewBox="0 0 12 12"><rect x="1" y="2.5" width="10" height="7" fill="#2328dd"/><path d="M1 2.5l5 4 5-4" fill="none" stroke="#fff" stroke-width="1"/></svg>info@v-t-s.com</li>
        <li><svg class="contact-icon" viewBox="0 0 12 12"><circle cx="6" cy="6" r="5" fill="#2328dd"/><path d="M1 6h10M6 1c-2 3-2 7 0 10M6 1c2 3 2 7 0 10" fill="none" stroke="#fff" stroke-width="0.8"/></svg>www.v-t-s.com</li>
      </ul>
    </div>
  </section>

  <section class="card card--back">
    <div class="back__brand"><span class="brand-name">Veltrix</span></div>
    <p class="service-list">
      Conveyors: Target sauce Applicators • Target Topping Applicators<br>
      Watrerfall Topping Applicators • Pepperoni • Meat Slicer • Applicators<br>
      Portion Controlled Filler Pumps • Dry Ingredient Applicators<br>
      Check Weigh Converyors • Portion Compensators
    </p>
  </section>
</body>
</html>
```